Business Card for beauty technology startup

Design Glowmi Business Card for a Beauty, based on the website identity and colors (https://www.glowmi-example.com).
Glowmi is a beauty tech startup that gathers helpful product info for beauty lovers and consumers (such as availability on stores, price range and product reviews) for makeup products. The card design must be young, colorful but clean, and very modern.

Target Market(s)

woman, 15-35

Industry/Entity Type

Cosmetics

Contact Information for Business Card

Full Name, address, phone

Font styles to use
Other font styles liked:
• Advent Pro

Colors
e34297
86cfc6
ffffff
5c5c5c
e8e8e8
e667a6
b2b2b2

Requirements
Must have
• One full colored side with a creative design and another with card info
• Use Color palette: #95C5C5 and/or #D38AA5
• Use fonts: Advent Pro
• Use website identity: https://www.glowmi-example.com
Nice to have
• If needed extra font: Roboto

```html
<!DOCTYPE html>
<html lang="en">
<head>
<meta charset="utf-8">
<title>Glowmi Business Card</title>
<link rel="stylesheet" href="https://fonts.googleapis.com/css2?family=Advent+Pro:wght@300;400&family=Roboto:wght@400;500&family=Open+Sans:wght@400&display=swap">
<style>
  :root {
    --bg: #e8e8e8;
    --card: #ffffff;
    --ink: #5c5c5c;
    --ink-strong: #3a3a3a;
    --muted: #b2b2b2;
    --pink: #e34297;
    --pink-soft: #e667a6;
    --rose: #d38aa5;
    --teal: #86cfc6;
    --teal-deep: #95c5c5;
    --shadow: rgba(0, 0, 0, 0.18);
  }
  * { box-sizing: border-box; margin: 0; padding: 0; }
  html, body {
    width: 1200px;
    height: 1021px;
    overflow: hidden;
    background: var(--bg);
  }
  .canvas { position: relative; width: 1200px; height: 1021px; }

  .card {
    position: absolute;
    width: 540px;
    height: 309px;
    box-shadow: 0 10px 30px var(--shadow);
    overflow: hidden;
  }
  .card--info { left: 80px; top: 120px; background: var(--card); color: var(--ink-strong); }
  .card--brand {
    left: 580px;
    top: 590px;
    background: linear-gradient(135deg, var(--pink) 0%, var(--pink-soft) 45%, var(--teal) 100%);
    color: var(--card);
  }

  .brand {
    display: flex;
    align-items: center;
    gap: 12px;
    font-family: "Advent Pro", sans-serif;
    font-weight: 300;
    letter-spacing: 0.18em;
    white-space: nowrap;
  }
  .brand__dot { border-radius: 50%; flex: none; }

  .card--info .brand {
    position: absolute;
    top: 28px;
    right: 34px;
    font-size: 30px;
    color: var(--pink);
  }
  .card--info .brand__dot { width: 28px; height: 28px; background: var(--teal); }

  .social {
    position: absolute;
    top: 80px;
    right: 50px;
    display: flex;
    gap: 22px;
  }
  .social__item { width: 11px; height: 11px; background: var(--teal); border-radius: 2px; }

  .person {
    position: absolute;
    left: 32px;
    top: 118px;
    padding-left: 14px;
    border-left: 8px solid var(--pink);
    font-family: "Roboto", sans-serif;
  }
  .person__name { font-size: 22px; font-weight: 500; line-height: 1.1; color: var(--ink-strong); }
  .person__title { font-size: 13px; color: var(--ink); margin-top: 2px; }

  .contact {
    position: absolute;
    left: 32px;
    bottom: 34px;
    font-family: "Open Sans", sans-serif;
    font-size: 13px;
    color: var(--ink);
    line-height: 1.45;
  }
  .contact__row { display: flex; gap: 8px; align-items: flex-start; }
  .contact__icon { width: 12px; height: 12px; margin-top: 3px; flex: none; color: var(--pink); }

  .card--info .web {
    position: absolute;
    right: 34px;
    top: 124px;
    font-family: "Open Sans", sans-serif;
    font-size: 13px;
    color: var(--ink);
  }
  .card--info .accent-band {
    position: absolute;
    left: 0;
    right: 0;
    bottom: 0;
    height: 8px;
    background: linear-gradient(90deg, var(--pink), var(--teal));
  }

  .card--brand .brand {
    position: absolute;
    left: 50%;
    top: 98px;
    transform: translateX(-50%);
    font-size: 50px;
  }
  .card--brand .brand__dot { width: 50px; height: 50px; border: 2px solid var(--card); }
  .card--brand .web {
    position: absolute;
    left: 0;
    right: 0;
    top: 196px;
    text-align: center;
    font-family: "Open Sans", sans-serif;
    font-size: 14px;
  }
</style>
</head>
<body>
<main class="canvas">
  <section class="card card--info" aria-label="Card front with contact details">
    <div class="brand"><span class="brand__dot"></span><span>GLOWMI</span></div>
    <div class="social" aria-label="Social links">
      <span class="social__item"></span>
      <span class="social__item"></span>
      <span class="social__item"></span>
      <span class="social__item"></span>
    </div>
    <div class="person">
      <p class="person__name">Your Name</p>
      <p class="person__title">Job Title</p>
    </div>
    <p class="web">www.glowmi-example.com</p>
    <div class="contact">
      <div class="contact__row">
        <svg class="contact__icon" viewBox="0 0 24 24" aria-hidden="true"><path fill="currentColor" d="M6.6 10.8a15 15 0 0 0 6.6 6.6l2.2-2.2a1 1 0 0 1 1-.25 11.4 11.4 0 0 0 3.6.57 1 1 0 0 1 1 1V20a1 1 0 0 1-1 1A17 17 0 0 1 3 4a1 1 0 0 1 1-1h3.5a1 1 0 0 1 1 1c0 1.25.2 2.45.57 3.57a1 1 0 0 1-.25 1z"/></svg>
        <span>000 000 0000</span>
      </div>
      <div class="contact__row">
        <svg class="contact__icon" viewBox="0 0 24 24" aria-hidden="true"><path fill="currentColor" d="M12 2a7 7 0 0 0-7 7c0 5.25 7 13 7 13s7-7.75 7-13a7 7 0 0 0-7-7zm0 9.5A2.5 2.5 0 1 1 12 6.5a2.5 2.5 0 0 1 0 5z"/></svg>
        <span>1450 Harbor Lane, suite 210<br>Bayview, Texas 70000</span>
      </div>
    </div>
    <div class="accent-band"></div>
  </section>

  <section class="card card--brand" aria-label="Card back with brand">
    <div class="brand"><span class="brand__dot"></span><span>GLOWMI</span></div>
    <p class="web">www.glowmi-example.com</p>
  </section>
</main>
</body>
</html>
```